MSA Plans

I would like to rebuild my brochure for the 3 business plans that I currently offer my clients. I would like to make it look much more modern & attractive to clients when choosing one of our service plans. If we can stick to a tech theme that would be great. Message me for anymore information.

```html
<!DOCTYPE html>
<html lang="en">
<head>
<meta charset="utf-8">
<title>MSA Plans</title>
<link href="https://fonts.googleapis.com/css2?family=Montserrat:wght@400;500;600;700&display=swap" rel="stylesheet">
<style>
:root{
  --orange:#ee7330;
  --black:#000;
  --white:#fff;
  --line:#fbe1d3;
  --green:#3ea54a;
  --red:#e2262a;
  --backdrop:#bdbec0;
  --ink:#111;
}
*{margin:0;padding:0;box-sizing:border-box}
html,body{width:1200px;height:881px;overflow:hidden}
body{background:var(--backdrop);font-family:'Montserrat',sans-serif;color:var(--ink);position:relative}
.page{position:absolute;top:88px;width:498px;height:705px;background:var(--white)}
.page--plans{left:79px}
.page--security{left:623px}
.brand{position:absolute;left:20px;top:30px;display:flex;align-items:center;gap:7px}
.brand-mark{width:14px;height:14px;background:var(--orange)}
.brand-name{font-size:22px;font-weight:600;letter-spacing:1.5px;color:var(--black)}
.plan-table{position:absolute;left:17px;top:93px;width:463px;border-collapse:separate;border-spacing:0;table-layout:fixed}
.plan-table th{background:var(--orange);color:var(--white);font-weight:500;font-size:10.2px;height:24px;text-align:center;border-left:1px solid var(--white)}
.plan-table th:first-child{text-align:left;padding-left:10px;border-left:0}
.plan-table td{height:20.2px;font-size:9px;text-align:center;border-bottom:1px solid var(--line);border-left:1px solid var(--line);vertical-align:middle;white-space:nowrap}
.plan-table td:first-child{text-align:left;padding-left:10px}
.plan-table td:last-child{border-right:1px solid var(--line)}
.plan-table .section td{background:var(--black);color:var(--white);font-size:10px;font-weight:500;height:18.5px;border:0;padding-left:10px}
.note{font-size:6.6px}
.icon{width:14px;height:14px;display:block;margin:0 auto}
.pricing td{background:var(--black);color:var(--white);height:auto;border:0;border-left:1px solid var(--white);font-size:8.8px;font-weight:500;line-height:16px;padding:4px 0}
.pricing td:first-child{border-left:0;color:var(--orange)}
.pricing .base{float:right;color:var(--white);text-align:center;width:50px;margin-right:12px}
.tall td{height:24px}
.pending{line-height:1;font-size:8.8px}
.contact-band{position:absolute;left:17px;top:620px;width:463px;height:55px;background:var(--orange);color:var(--white);text-align:center;padding-top:10px}
.contact-band .company{font-size:10.5px;font-weight:600;line-height:13px}
.contact-band .details{font-size:8.8px;font-weight:500;line-height:10.5px}
</style>
</head>
<body>
<svg width="0" height="0" style="position:absolute">
  <defs>
    <symbol id="tick" viewBox="0 0 20 20"><circle cx="10" cy="11" r="7.5" fill="none" stroke="var(--green)" stroke-width="1.8"/><path d="M6 10.5l3.5 4L16 2" fill="none" stroke="var(--green)" stroke-width="2.2" stroke-linecap="round" stroke-linejoin="round"/></symbol>
    <symbol id="cross" viewBox="0 0 20 20"><circle cx="10" cy="10" r="7.5" fill="none" stroke="var(--red)" stroke-width="1.8"/><path d="M7 6.5l6 7M13 6.5l-6 7" stroke="var(--red)" stroke-width="2" stroke-linecap="round"/></symbol>
  </defs>
</svg>

<section class="page page--plans">
  <div class="brand"><span class="brand-name">NORTHDESK</span><span class="brand-mark"></span></div>
  <table class="plan-table">
    <colgroup><col style="width:233px"><col style="width:75px"><col style="width:79px"><col style="width:76px"></colgroup>
    <thead><tr><th>Managed Services Agreement</th><th>Essential</th><th>Business</th><th>Professional</th></tr></thead>
    <tbody>
      <tr class="section"><td colspan="4">Support</td></tr>
      <tr><td>Unlimited Remote Support 7am to 6pm</td><td><svg class="icon"><use href="#tick"/></svg></td><td><svg class="icon"><use href="#tick"/></svg></td><td><svg class="icon"><use href="#tick"/></svg></td></tr>
      <tr><td>3rd Party Vendor Support</td><td><svg class="icon"><use href="#tick"/></svg></td><td><svg class="icon"><use href="#tick"/></svg></td><td><svg class="icon"><use href="#tick"/></svg></td></tr>
      <tr><td>Reactive Onsite Support 8am to 5pm</td><td>VIP Rates</td><td></td><td><svg class="icon"><use href="#tick"/></svg></td></tr>
      <tr><td>After-Hours Support</td><td>VIP Rates</td><td>VIP Rates</td><td><svg class="icon"><use href="#tick"/></svg></td></tr>
      <tr class="section"><td colspan="4">Service</td></tr>
      <tr><td>Guaranteed SLA Response Times</td><td><svg class="icon"><use href="#tick"/></svg></td><td><svg class="icon"><use href="#tick"/></svg></td><td><svg class="icon"><use href="#tick"/></svg></td></tr>
      <tr><td>24x7 Website &amp; Infrastructure Monitoring</td><td><svg class="icon"><use href="#tick"/></svg></td><td><svg class="icon"><use href="#tick"/></svg></td><td><svg class="icon"><use href="#tick"/></svg></td></tr>
      <tr><td>Secure Web Content Filtering</td><td><svg class="icon"><use href="#tick"/></svg></td><td><svg class="icon"><use href="#tick"/></svg></td><td><svg class="icon"><use href="#tick"/></svg></td></tr>
      <tr><td>Backup Monitoring</td><td><svg class="icon"><use href="#tick"/></svg></td><td><svg class="icon"><use href="#tick"/></svg></td><td><svg class="icon"><use href="#tick"/></svg></td></tr>
      <tr><td>Vantix OS Patching &amp; Updating</td><td><svg class="icon"><use href="#tick"/></svg></td><td><svg class="icon"><use href="#tick"/></svg></td><td><svg class="icon"><use href="#tick"/></svg></td></tr>
      <tr><td>CEO / MD Home Tech Support</td><td><svg class="icon"><use href="#tick"/></svg></td><td><svg class="icon"><use href="#tick"/></svg></td><td><svg class="icon"><use href="#tick"/></svg></td></tr>
      <tr><td>Monthly Tech Site Visit</td><td><svg class="icon"><use href="#cross"/></svg></td><td>Quarterly</td><td>Monthly</td></tr>
      <tr><td>Short Term Loan Equipment</td><td><svg class="icon"><use href="#cross"/></svg></td><td>1 Month</td><td>3 Months</td></tr>
      <tr><td>Adds / Moves / Changes (Staff)</td><td><svg class="icon"><use href="#tick"/></svg></td><td><svg class="icon"><use href="#tick"/></svg></td><td><svg class="icon"><use href="#tick"/></svg></td></tr>
      <tr><td>Adds / Moves / Changes (Workstations)</td><td>VIP Rates</td><td>VIP Rates</td><td><svg class="icon"><use href="#tick"/></svg></td></tr>
      <tr class="section"><td colspan="4">Management</td></tr>
      <tr><td>Asset and Warranty Tracking &amp; Reporting</td><td><svg class="icon"><use href="#tick"/></svg></td><td><svg class="icon"><use href="#tick"/></svg></td><td><svg class="icon"><use href="#tick"/></svg></td></tr>
      <tr><td>Comprehensive IT Documentation</td><td><svg class="icon"><use href="#tick"/></svg></td><td><svg class="icon"><use href="#tick"/></svg></td><td><svg class="icon"><use href="#tick"/></svg></td></tr>
      <tr><td>Technology Strategy Meeting</td><td>Annual</td><td>Quarterly</td><td>Monthly</td></tr>
      <tr><td>Technology Business Review Meeting</td><td>Annual</td><td>Bi Annual</td><td>Quarterly</td></tr>
      <tr><td>IT Policy Templates</td><td><svg class="icon"><use href="#cross"/></svg></td><td><svg class="icon"><use href="#tick"/></svg></td><td><svg class="icon"><use href="#tick"/></svg></td></tr>
      <tr class="section"><td colspan="4">Training</td></tr>
      <tr><td>End User Training Materials</td><td><svg class="icon"><use href="#cross"/></svg></td><td><svg class="icon"><use href="#cross"/></svg></td><td><svg class="icon"><use href="#tick"/></svg></td></tr>
      <tr><td>Security Awareness Training</td><td><svg class="icon"><use href="#tick"/></svg></td><td><svg class="icon"><use href="#tick"/></svg></td><td><svg class="icon"><use href="#tick"/></svg></td></tr>
      <tr class="pricing"><td>RRP / User<br>Minimum User Count<br>Minimum Monthly Commit</td><td>$110<br>5<br>$550</td><td>$130<br>5<br>$650</td><td>$165<br>5<br>$825</td></tr>
    </tbody>
  </table>
</section>

<section class="page page--security">
  <div class="brand"><span class="brand-name">NORTHDESK</span><span class="brand-mark"></span></div>
  <table class="plan-table">
    <colgroup><col style="width:310px"><col style="width:76px"><col style="width:77px"></colgroup>
    <thead><tr><th>Cybersecurity Packages</th><th>Business</th><th>Professional</th></tr></thead>
    <tbody>
      <tr><td>Compliance with NCSA Core Eight Maturity</td><td><svg class="icon"><use href="#tick"/></svg></td><td><svg class="icon"><use href="#tick"/></svg></td></tr>
      <tr><td>Security Standard - <span class="note">Alignment to Northdesk V365 Security Policy &amp; Reporting</span></td><td><svg class="icon"><use href="#tick"/></svg></td><td><svg class="icon"><use href="#tick"/></svg></td></tr>
      <tr><td>24x7 Security Operations Centre (SOC) - Monitoring Vantix Office</td><td><svg class="icon"><use href="#tick"/></svg></td><td><svg class="icon"><use href="#tick"/></svg></td></tr>
      <tr><td>Dark Web Scanning</td><td><svg class="icon"><use href="#tick"/></svg></td><td><svg class="icon"><use href="#tick"/></svg></td></tr>
      <tr><td>Cloud Email Filtering</td><td><svg class="icon"><use href="#tick"/></svg></td><td><svg class="icon"><use href="#tick"/></svg></td></tr>
      <tr><td>Vantix 365 Backup</td><td><svg class="icon"><use href="#tick"/></svg></td><td><svg class="icon"><use href="#tick"/></svg></td></tr>
      <tr><td>Automated Email Signatures</td><td><svg class="icon"><use href="#tick"/></svg></td><td><svg class="icon"><use href="#tick"/></svg></td></tr>
      <tr><td>Endpoint Protection with EDR - Workstations &amp; Servers</td><td><svg class="icon"><use href="#tick"/></svg></td><td><svg class="icon"><use href="#tick"/></svg></td></tr>
      <tr><td>3rd Party Applications Updating</td><td><svg class="icon"><use href="#cross"/></svg></td><td><svg class="icon"><use href="#tick"/></svg></td></tr>
      <tr><td>24x7 Security Operations Centre (SOC) - <span class="note">Monitoring Endpoints and Servers</span></td><td><svg class="icon"><use href="#cross"/></svg></td><td><svg class="icon"><use href="#tick"/></svg></td></tr>
      <tr><td>Privileged Access Management &amp; Application Whitelisting</td><td><svg class="icon"><use href="#cross"/></svg></td><td><svg class="icon"><use href="#tick"/></svg></td></tr>
      <tr><td>Internal Vulnerability Scanning</td><td><svg class="icon"><use href="#cross"/></svg></td><td><svg class="icon"><use href="#tick"/></svg></td></tr>
      <tr class="tall"><td>Backup &amp; Disaster Recovery to comply with <span class="note">NCSA Core Eight Maturity Level 1</span></td><td><svg class="icon"><use href="#cross"/></svg></td><td class="pending">Pending<br>Assessment</td></tr>
      <tr><td colspan="3" style="height:8px;border:0"></td></tr>
      <tr class="pricing"><td><span class="base">$110<br>5<br>$550</span>RRP / User<br>Minimum User Count<br>Minimum Monthly Commit</td><td>$35<br>5<br>$175</td><td>$60<br>5<br>$300</td></tr>
    </tbody>
  </table>
  <footer class="contact-band">
    <p class="company">NORTHDESK COMPUTER SERVICES PTY LTD | ABN: 41 582 903 117</p>
    <p class="details">northdeskit.com.au | service@northdeskit.com.au</p>
    <p class="details">12/48 Carrow St, Westmere Park, VIC, 3040 | 1300 555 018</p>
  </footer>
</section>
</body>
</html>
```